metal roofing website

I have several domain names and a website that has been built. I need someone to recreate essentially the same website and change some photos and basic design to create the new sites. I have all of the files and c panel access to the lucky winner. If you can do a good job at a fair price I will have 100's of sites to send to you very soon. I have the site built and have all files just need it recreated on my server. the current site is www.dorvanemetalinc.com I am looking to get this done ASAP!!!

```html
<!DOCTYPE html>
<html lang="en">
<head>
<meta charset="utf-8">
<title>Dorvane Metal Inc. – Roofing</title>
<link href="https://fonts.googleapis.com/css2?family=Montserrat:wght@400;500;600;700&family=Open+Sans:wght@400;600&display=swap" rel="stylesheet">
<style>
:root{
  --orange:#e2572a;
  --yellow:#f2b705;
  --dark:#232323;
  --dark2:#2c2c2e;
  --dark3:#333336;
  --panel:#3a3a3d;
  --line:#e6e6e6;
  --muted:#9a9a9a;
  --white:#ffffff;
}
*{box-sizing:border-box;margin:0;padding:0}
html,body{width:1200px;height:2936px;overflow:hidden}
body{font-family:"Open Sans",Arial,sans-serif;color:#444;background:var(--white);position:relative}
.abs{position:absolute}
h1,h2,h3,.mont{font-family:"Montserrat",Arial,sans-serif}

.topbar{left:0;top:0;width:1200px;height:43px;background:var(--dark);color:#ddd;font-size:12px}
.topbar .info{left:160px;top:13px;display:flex;gap:28px;align-items:center}
.topbar .info span{display:flex;gap:8px;align-items:center}
.topbar .social{left:910px;top:15px;display:flex;gap:14px}
.topbar .social i{display:block;width:10px;height:10px;border-radius:50%;background:#ddd}

.nav{left:0;top:43px;width:1200px;height:78px;background:var(--dark2)}
.brand{display:flex;align-items:center;gap:8px;font-family:"Montserrat",sans-serif;font-weight:700;font-size:15px;line-height:17px;color:var(--orange);width:110px}
.nav .brand{left:156px;top:20px}
.brand b{width:14px;height:14px;background:var(--orange);display:block;flex:none}
.menu{left:318px;top:32px;display:flex;gap:36px;font-family:"Montserrat",sans-serif;font-size:12px;letter-spacing:1px;color:#eee;font-weight:500}
.call{left:924px;top:20px;font-size:12px;color:#eee;line-height:22px}
.call strong{color:var(--orange);font-family:"Montserrat",sans-serif;font-size:13px}

.hero{left:0;top:121px;width:1200px;height:433px;background:linear-gradient(90deg,#6d5a45 0%,#8a7a66 40%,#5f6f7d 70%,#7c8894 100%)}
.hero .txt{left:0;top:35px;width:1200px;text-align:center;color:var(--white);font-family:"Montserrat",sans-serif}
.hero .welcome{font-size:14px;font-weight:600}
.hero .l1{font-size:48px;font-weight:500;margin-top:14px;line-height:56px}
.hero .l1 em,.hero .l2 em{font-style:normal;color:var(--yellow);font-weight:700}
.hero .l2{font-size:48px;font-weight:500;line-height:60px}
.hero .down{left:582px;top:210px}

.features{left:143px;top:446px;width:920px;height:180px;display:flex}
.features .f{flex:1;background:var(--orange);color:var(--white);text-align:center;padding-top:58px;font-size:14px;border-left:1px solid rgba(255,255,255,.2)}
.features .f:first-child{background:var(--dark3);border:0;position:relative}
.features .f:first-child:after{content:"";position:absolute;left:86px;bottom:8px;width:12px;height:3px;background:var(--orange)}
.features svg{display:block;margin:0 auto 16px}

.sect-title{left:0;width:1200px;text-align:center;font-size:22px;font-weight:500;color:#333}
.sect-title em{font-style:normal;color:var(--orange)}
.sect-title:after{content:"";display:block;width:12px;height:3px;background:var(--orange);margin:10px auto 0}
.sect-lead{left:390px;width:420px;text-align:center;font-size:11.5px;line-height:24px;color:#555}

.grid{left:137px;top:855px;width:930px;height:535px;display:grid;grid-template-columns:repeat(3,1fr);grid-template-rows:repeat(2,1fr)}
.svc{text-align:center;padding:46px 36px 0;border-right:1px solid var(--line);border-bottom:1px solid var(--line)}
.svc:nth-child(3n){border-right:0}
.svc:nth-child(n+4){border-bottom:0}
.svc h3{font-family:"Open Sans",sans-serif;font-weight:400;font-size:13px;color:#555;margin-top:20px}
.svc h3:after{content:"";display:block;width:10px;height:2px;background:var(--orange);margin:12px auto 0}
.svc p{font-size:11px;color:#b5b5b5;line-height:23px;margin-top:14px}

.process-photo{left:0;top:1425px;width:603px;height:522px;background:linear-gradient(135deg,#5a6068,#8b8f95 50%,#6c7176)}
.play{left:288px;top:1666px}
.process{left:603px;top:1425px;width:597px;height:522px;background:var(--dark2)}
.process h2{left:60px;top:34px;font-size:21px;font-weight:500;color:var(--white)}
.process h2 em{font-style:normal;color:var(--yellow)}
.process h2:after{content:"";display:block;width:12px;height:3px;background:var(--orange);margin-top:8px}
.process .lead{left:60px;top:92px;width:420px;font-size:11.5px;line-height:23px;color:#eee}
.acc{left:60px;top:183px;width:472px}
.acc .item{height:40px;background:var(--panel);margin-bottom:5px;color:#eee;font-family:"Montserrat",sans-serif;font-size:11px;font-weight:600;display:flex;align-items:center;justify-content:space-between;padding:0 14px 0 10px}
.acc .item.open{background:var(--orange);color:var(--white);margin-bottom:0}
.acc .body{font-size:11px;color:#ddd;line-height:23px;padding:14px 20px 18px 30px;border-left:1px solid #555;margin-left:4px;margin-bottom:5px}

.quote-bg{left:0;top:1947px;width:1200px;height:533px;background:linear-gradient(90deg,#2d2d2f,#3d3d40 60%,#2d2d2f)}
.worker{left:724px;top:1947px;width:333px;height:533px;background:linear-gradient(180deg,#c9a23a 0%,#a88453 40%,#7d6a58 100%);border-radius:160px 160px 0 0}
.card{left:141px;top:2016px;width:305px;height:436px;background:var(--white)}
.card .tab{height:38px;border-bottom:1px solid #eee;text-align:center;line-height:38px;font-family:"Montserrat",sans-serif;font-size:10.5px;font-weight:700;letter-spacing:.5px;color:#333}
.card .head{background:var(--dark2);height:118px;text-align:center;color:var(--white);padding-top:20px}
.card .head h3{font-size:19px;font-weight:500}
.card .head p{font-size:11px;line-height:22px;margin:8px auto 0;width:240px;color:#ddd}
.card form{padding:22px 28px 0}
.card .in{height:34px;border:1px solid #e5e5e5;font-size:10.5px;color:#666;padding:9px 10px;margin-bottom:6px}
.card .ta{height:74px}
.card .btn{height:40px;background:var(--orange);color:var(--white);text-align:center;line-height:40px;font-family:"Montserrat",sans-serif;font-weight:700;font-size:11px;letter-spacing:1px;margin-top:12px}
.doing{left:460px;top:2088px;width:220px;color:var(--white)}
.doing h2{font-size:21px;font-weight:500;line-height:24px}
.doing h2 em{font-style:normal;color:var(--orange)}
.doing h2:after{content:"";display:block;width:12px;height:3px;background:var(--orange);margin-top:8px}
.doing p{font-size:11px;line-height:22px;margin-top:18px}
.doing .more{display:inline-block;background:var(--yellow);color:var(--white);font-family:"Montserrat",sans-serif;font-size:10.5px;font-weight:700;letter-spacing:.5px;padding:14px 24px;margin-top:30px}
.totop{left:584px;top:2462px}

.footer{left:0;top:2480px;width:1200px;height:456px;background:var(--dark2);color:#bbb}
.footer .brand{left:151px;top:30px}
.footer .about{left:151px;top:80px;width:290px;font-size:11px;line-height:22px}
.footer .soc{left:156px;top:228px;display:flex;gap:22px}
.footer .soc i{display:block;width:10px;height:10px;border-radius:50%;background:#ddd}
.footer h4{font-family:"Montserrat",sans-serif;font-size:13px;font-weight:500;color:var(--white)}
.hours{left:460px;top:90px}
.hours h4:after{content:"";display:block;width:12px;height:3px;background:var(--orange);margin:8px 0 20px}
.hours table{border-collapse:collapse;font-size:10.5px;color:#aaa}
.hours td{height:30px;padding-right:30px}
.news{left:770px;top:90px;width:286px}
.news h4{margin-bottom:34px}
.news .in{height:34px;border:1px solid #4a4a4d;font-size:10.5px;color:#999;padding:9px 10px;margin-bottom:8px}
.news .row{display:flex;gap:8px}
.news .ta{flex:1;height:54px}
.news .send{width:54px;height:54px;background:var(--orange);color:var(--white);font-family:"Montserrat",sans-serif;font-size:12px;font-weight:600;text-align:center;line-height:54px}
.bottom{left:151px;top:2883px;width:906px;height:53px;background:#262628;display:flex;justify-content:space-between;align-items:center;padding:0 20px 0 24px;font-size:11px;color:#ccc}
.bottom nav{display:flex;gap:14px}
.bottom span{color:#888}
</style>
</head>
<body>

<header>
  <div class="abs topbar">
    <div class="abs info">
      <span><svg width="14" height="14" viewBox="0 0 14 14"><circle cx="7" cy="7" r="6" fill="none" stroke="#ddd"/><path d="M7 3v4l3 2" stroke="#ddd" fill="none"/></svg>Mon-Sat: 9.00-18.00</span>
      <span><svg width="14" height="10" viewBox="0 0 14 10"><rect x=".5" y=".5" width="13" height="9" fill="none" stroke="#ddd"/><path d="M1 1l6 5 6-5" stroke="#ddd" fill="none"/></svg>info@dorvanemetal.com</span>
    </div>
    <div class="abs social"><i></i><i></i><i></i><i></i><i></i><i></i></div>
  </div>
  <div class="abs nav">
    <div class="abs brand"><b></b><span>DORVANE<br>METAL</span></div>
    <nav class="abs menu"><span>HOME</span><span>ABOUT US</span><span>SERVICES</span><span>GALLERY</span><span>CONTACT US</span></nav>
    <div class="abs call">Call Us<br><strong>+ 555 014 2290</strong></div>
  </div>
</header>

<section class="abs hero" role="img" aria-label="Smiling roofer in hard hat and safety glasses giving a thumbs up, with coworkers behind">
  <div class="abs txt">
    <div class="welcome">Welcome to Dorvane Metal Inc.</div>
    <h1 class="l1">we are <em>ROOFER</em></h1>
    <div class="l2">helping <em>YOUR ROOFING</em></div>
  </div>
  <svg class="abs down" width="36" height="40" viewBox="0 0 36 40"><path d="M4 16v20h28V16" stroke="#fff" stroke-width="2" fill="none"/><path d="M18 4v22M11 19l7 7 7-7" stroke="#fff" stroke-width="2" fill="none"/></svg>
</section>

<div class="abs features">
  <div class="f"><svg width="36" height="38" viewBox="0 0 36 38" fill="none" stroke="#fff" stroke-width="2"><path d="M10 4h16v10a8 8 0 0 1-16 0z"/><path d="M10 8H4a6 6 0 0 0 6 8M26 8h6a6 6 0 0 1-6 8M18 22v8M11 34h14"/></svg>10+ Years Experiencee</div>
  <div class="f"><svg width="36" height="38" viewBox="0 0 36 38" fill="none" stroke="#fff" stroke-width="2"><path d="M9 14a9 9 0 0 1 18 0z"/><circle cx="18" cy="19" r="5"/><path d="M6 36a12 12 0 0 1 24 0"/></svg>Expert &amp; Professional</div>
  <div class="f"><svg width="36" height="38" viewBox="0 0 36 38" fill="none" stroke="#fff" stroke-width="2"><path d="M13 4h10l-3 7h-4z"/><path d="M16 11c-8 4-12 12-10 19 1 4 5 6 12 6s11-2 12-6c2-7-2-15-10-19"/><text x="18" y="30" font-size="12" fill="#fff" stroke="none" text-anchor="middle" font-family="Montserrat">$</text></svg>Free Cost Inspections</div>
  <div class="f"><svg width="36" height="38" viewBox="0 0 36 38" fill="none" stroke="#fff" stroke-width="2"><circle cx="18" cy="19" r="14"/><text x="18" y="23" font-size="11" fill="#fff" stroke="none" text-anchor="middle" font-family="Montserrat" font-weight="700">24</text></svg>24 / 7 Open Services</div>
  <div class="f"><svg width="36" height="38" viewBox="0 0 36 38" fill="none" stroke="#fff" stroke-width="2"><rect x="5" y="6" width="26" height="26"/><path d="M5 14h26M5 22h26M14 6v26M22 6v26"/></svg>Exterior Expertises</div>
</div>

<main>
  <h2 class="abs sect-title" style="top:708px"><em>OUR</em> SERVICES</h2>
  <p class="abs sect-lead" style="top:764px">Suspendisse laoreet tempus auctor. Sed sed neque nibh. Ut quis arcu quis quam vehicula convallis sed non tellus. Lorem ipsum dolor sit amet</p>

  <div class="abs grid">
    <div class="svc"><svg width="32" height="28" viewBox="0 0 32 28" fill="none" stroke="#e2572a" stroke-width="2"><path d="M2 6h8l12 16h8M2 22h8l12-16h8M26 2l4 4-4 4M26 18l4 4-4 4"/></svg><h3>Roof Replacement</h3><p>Lay a row of starter shingles down both sides of the roof as well and secure those in place using roofing nails...</p></div>
    <div class="svc"><svg width="32" height="28" viewBox="0 0 32 28" fill="none" stroke="#e2572a" stroke-width="2"><path d="M9 10a7 7 0 0 1 14 0z"/><circle cx="16" cy="14" r="4"/><path d="M6 27a10 10 0 0 1 20 0"/></svg><h3>Roof Maintenance</h3><p>Lay a row of starter shingles down both sides of the roof as well and secure those in place using roofing nails...</p></div>
    <div class="svc"><svg width="32" height="28" viewBox="0 0 32 28" fill="none" stroke="#e2572a" stroke-width="2"><path d="M4 14L16 3l12 11M8 11v15h16V11"/><circle cx="16" cy="17" r="3"/></svg><h3>Roof Inspections</h3><p>Lay a row of starter shingles down both sides of the roof as well and secure those in place using roofing nails...</p></div>
    <div class="svc"><svg width="32" height="28" viewBox="0 0 32 28" fill="none" stroke="#e2572a" stroke-width="2"><path d="M3 8h26M3 13h26M3 18h26M3 23h26"/></svg><h3>Roof Leak Maintenance</h3><p>Lay a row of starter shingles down both sides of the roof as well and secure those in place using roofing nails...</p></div>
    <div class="svc"><svg width="32" height="28" viewBox="0 0 32 28" fill="none" stroke="#e2572a" stroke-width="2"><path d="M3 5l8 3 10-3 8 3v17l-8-3-10 3-8-3zM11 8v17M21 5v17"/></svg><h3>Green Roof Installation</h3><p>Lay a row of starter shingles down both sides of the roof as well and secure those in place using roofing nails...</p></div>
    <div class="svc"><svg width="32" height="28" viewBox="0 0 32 28" fill="none" stroke="#e2572a" stroke-width="2"><circle cx="20" cy="10" r="7"/><path d="M20 6v4h3M4 24l6-6 4 2 4-4M4 24h10"/></svg><h3>Emergency Response 24 / 7</h3><p>Lay a row of starter shingles down both sides of the roof as well and secure those in place using roofing nails...</p></div>
  </div>

  <section>
    <div class="abs process-photo" role="img" aria-label="Woman engineer in yellow hard hat and safety vest holding blueprints on a construction site"></div>
    <svg class="abs play" width="38" height="38" viewBox="0 0 38 38"><circle cx="19" cy="19" r="17" fill="#fff" stroke="#333" stroke-width="2"/><path d="M15 12l11 7-11 7z" fill="#333"/></svg>
    <div class="abs process">
      <h2 class="abs"><em>OUR</em> PROCESS</h2>
      <p class="abs lead">Suspendisse laoreet tempus auctor. Sed sed neque nibh. Ut quis arcu quis quam vehicula convallis sed non tellus. Lorem ipsum dolor sit amet</p>
      <div class="abs acc">
        <div class="item open">01. Visiting on Your Space<svg width="10" height="6" viewBox="0 0 10 6"><path d="M1 5l4-4 4 4" stroke="#fff" fill="none"/></svg></div>
        <div class="body">Lorem ipsum dolor sit amet, consectetur adipiscing elit. Nam eu porta lacus, a vestibulum tortor. Etiam finibus id nisi vitae luctus. Sed efficitur, ipsum at semper ultrices, turpis mi conue libero, in suscipit arcu augue at arcu.</div>
        <div class="item">02. Giving Incharge to the Right Person<svg width="10" height="6" viewBox="0 0 10 6"><path d="M1 1l4 4 4-4" stroke="#ccc" fill="none"/></svg></div>
        <div class="item">03. Working Like Personal Work<svg width="10" height="6" viewBox="0 0 10 6"><path d="M1 1l4 4 4-4" stroke="#ccc" fill="none"/></svg></div>
        <div class="item">04. Finish Project Happy Movement<svg width="10" height="6" viewBox="0 0 10 6"><path d="M1 1l4 4 4-4" stroke="#ccc" fill="none"/></svg></div>
      </div>
    </div>
  </section>

  <section>
    <div class="abs quote-bg" role="img" aria-label="Dim construction site with scaffolding beams"></div>
    <div class="abs worker" role="img" aria-label="Smiling builder in yellow hard hat holding a hammer and wooden planks"></div>
    <div class="abs card">
      <div class="tab">WELCOME TO ROOFERS</div>
      <div class="head"><h3>Get a Free Quote</h3><p>Vestibulum felis quam, egestas fermentum elit et tristique, consequat nisi</p></div>
      <form>
        <div class="in">First Name</div>
        <div class="in">Email</div>
        <div class="in ta">Message</div>
        <div class="btn">SUBMIT</div>
      </form>
    </div>
    <div class="abs doing">
      <h2><em>WHAT WE</em> DOING<br>FOR YOU</h2>
      <p>Suspendisse laoreet tempus auctor. Sed sed neque nibh. Ut quis arcu quis quam vehicula convallis hello sed non tellus. Lorem ipsum dolor sit amet Lipsum Dolar.</p>
      <span class="more">READ MORE</span>
    </div>
  </section>
</main>

<footer class="abs footer">
  <div class="abs brand"><b></b><span>DORVANE<br>METAL</span></div>
  <p class="abs about">Donec pulvinar suscipit sapien nec blandit. Curabitur nunc eros, semper nisl aliquam rutrum neque. Mauris eleifend Donec pulvinar suscipit sapien nec blandit. Curabitur nunc eros, semper nisl aliquam rutrum neque. Mauris eleifend. nisl aliquam rutrum neque.</p>
  <div class="abs soc"><i></i><i></i><i></i><i></i><i></i></div>
  <div class="abs hours">
    <h4>WORKING HOURS</h4>
    <table>
      <tr><td>Monday</td><td>9:00 AM – 7:00 PM</td></tr>
      <tr><td>Tuesday</td><td>9:00 AM – 7:00 PM</td></tr>
      <tr><td>Wednesday</td><td>9:00 AM – 7:00 PM</td></tr>
      <tr><td>Thursday</td><td>9:00 AM – 7:00 PM</td></tr>
      <tr><td>Friday</td><td>9:00 AM – 7:00 PM</td></tr>
      <tr><td>Saturday</td><td>9:00 AM – 7:00 PM</td></tr>
      <tr><td>Sunday</td><td>Closed</td></tr>
    </table>
  </div>
  <div class="abs news">
    <h4>Newsletter</h4>
    <div class="in">Email</div>
    <div class="row"><div class="in ta">Message</div><div class="send">Send</div></div>
  </div>
</footer>
<svg class="abs totop" width="32" height="32" viewBox="0 0 32 32"><circle cx="16" cy="16" r="16" fill="#e2572a"/><path d="M11 18l5-5 5 5" stroke="#fff" stroke-width="2" fill="none"/></svg>
<div class="abs bottom">
  <nav><a>Pages</a><a>Services</a><a>Our Work</a><a>Blog</a><a>Contact Us</a></nav>
  <span>Copyright © 2017 Dorvane Metal Inc. All rights reserved.</span>
</div>

</body>
</html>
```